Webdesign für Importeur von Tierbedarfsartikeln
Zielgruppe
Wir importieren Tierbedarfsartikel und verkaufen sie ausschließlich online. Zielgruppe sind in erster Linie Katzenhalter.
Aufgabenstellung
Es gibt eine bestehende Webseite www.pfotenhain24.de Sie wurde bei Webrono erstellt und ist aktiv. Die Seite soll eine professionelle Ansicht erhalten. Schön wären edle Farben, nicht kunterbunt. Wichtig in dem Zusammenhang ist eben, dass sich derjenige mit dem Webronokonzept auskennt.
Dieser Auftrag wird Folgeaufträge erhalten, sprich Logo, Werbeflyer usw. Bilder der Produkte sind vorhanden.

```html
<!DOCTYPE html>
<html lang="de">
<head>
<meta charset="utf-8">
<title>Pfotenhain24 – Produktkatalog</title>
<link href="https://fonts.googleapis.com/css2?family=Karla:wght@400;500;600&family=Libre+Baskerville:wght@400&display=swap" rel="stylesheet">
<style>
  :root{
    --ink:#2b2426;
    --muted:#6f5a62;
    --pink:#e8a9bf;
    --pink-soft:#f4c6d5;
    --pink-text:#e58aaa;
    --price:#d6557d;
    --bg-soft:#fbf3f5;
    --line:#c9bcc1;
    --white:#ffffff;
    --green:#5ccf4e;
    --red:#dc4a4a;
  }
  *{box-sizing:border-box;margin:0;padding:0}
  html,body{width:1197px;height:1200px;overflow:hidden;background:var(--white)}
  body{font-family:"Karla",sans-serif;color:var(--ink)}
  .page{width:1440px;height:1440px;transform:scale(0.83125,0.83333);transform-origin:0 0;position:relative}
  .site-header{height:88px;position:relative;background:var(--white)}
  .brand,.main-nav a{position:absolute;top:34px;font-size:16px;letter-spacing:.3px;color:var(--ink);text-decoration:none}
  .brand{left:112px}
  .main-nav a.active{color:var(--pink-text)}
  .search{position:absolute;left:700px;top:24px;width:375px;height:40px;border:1px solid #cfc6c9;border-radius:3px;display:flex;align-items:center;padding-left:12px;gap:10px;color:#9a8d92;font-size:14px}
  .header-action{position:absolute;top:12px;text-align:center;font-size:14px;color:var(--muted)}
  .header-action svg{display:block;margin:0 auto 10px}
  .catalog{position:absolute;top:88px;left:0;width:1440px;height:1008px;background:var(--bg-soft)}
  .catalog h1{position:absolute;left:112px;top:36px;font-family:"Libre Baskerville",serif;font-weight:400;font-size:29px;color:var(--ink)}
  .filters{position:absolute;right:112px;top:40px;display:flex;gap:20px}
  .filters span{background:var(--pink-soft);color:var(--white);font-size:14px;padding:6px 12px;border-radius:3px;letter-spacing:.3px}
  .filters span.active{background:var(--pink-text)}
  .catalog hr{position:absolute;left:112px;top:86px;width:1216px;border:0;border-top:1px solid var(--line)}
  .grid{position:absolute;left:112px;top:120px;display:grid;grid-template-columns:repeat(4,280px);gap:32px}
  .card{background:var(--white);border-radius:14px;overflow:hidden;height:412px;display:flex;flex-direction:column;align-items:center}
  .card .photo{width:280px;height:220px}
  .card h2{font-weight:500;font-size:17px;line-height:28px;text-align:center;height:72px;display:flex;align-items:center;padding:0 12px;margin-top:4px}
  .price{color:var(--price);font-size:17px;font-weight:500;margin-top:0}
  .stock{font-size:13px;margin-top:12px;display:flex;align-items:center;gap:8px}
  .stock i{width:11px;height:11px;border-radius:50%;background:var(--green);display:inline-block}
  .stock.out i{background:var(--red)}
  .btn{margin-top:10px;width:248px;height:44px;border-radius:10px;background:var(--pink);color:var(--white);font-size:16px;letter-spacing:.4px;display:flex;align-items:center;justify-content:center}
  .site-footer{position:absolute;top:1096px;left:0;width:1440px;height:344px}
  .col{position:absolute;top:34px;font-size:14px;letter-spacing:.3px}
  .col h3{font-weight:400;font-size:14px;color:var(--ink);margin-bottom:18px}
  .col a{display:block;color:var(--muted);text-decoration:none;margin-bottom:14px}
  .newsletter{position:absolute;left:736px;top:72px;width:528px;text-align:center;font-size:14px;line-height:20px;color:var(--ink)}
  .newsletter form{display:flex;gap:8px;margin-top:34px}
  .newsletter .field{width:341px;height:40px;border:1px solid #cfc6c9;border-radius:3px;text-align:left;padding:10px 12px;color:#9a8d92;font-size:14px}
  .newsletter .submit{width:179px;height:40px;background:var(--pink);color:var(--white);border-radius:3px;font-size:14px;display:flex;align-items:center;justify-content:center;letter-spacing:.3px}
  .site-footer hr{position:absolute;left:112px;top:264px;width:1216px;border:0;border-top:1px solid var(--line)}
  .social{position:absolute;left:112px;top:296px;display:flex;gap:16px}
  .social span{width:20px;height:20px;border-radius:50%;background:#8e7f85}
  .legal{position:absolute;right:112px;top:298px;display:flex;gap:33px;font-size:14px;letter-spacing:.3px;color:var(--ink)}
</style>
</head>
<body>
<div class="page">
  <header class="site-header">
    <a class="brand" href="#">Pfotenhain24</a>
    <nav class="main-nav">
      <a href="#" class="active" style="left:258px">Produktkatalog</a>
      <a href="#" style="left:433px">Sale</a>
      <a href="#" style="left:526px">Kontakt</a>
    </nav>
    <div class="search">
      <svg width="18" height="18" viewBox="0 0 18 18"><circle cx="7.5" cy="7.5" r="6" fill="none" stroke="#6f5a62" stroke-width="1.8"/><line x1="12" y1="12" x2="17" y2="17" stroke="#6f5a62" stroke-width="1.8"/></svg>
      Suche
    </div>
    <div class="header-action" style="left:1190px">
      <svg width="16" height="20" viewBox="0 0 16 20"><circle cx="8" cy="5" r="4.5" fill="#6f5a62"/><path d="M0 19c0-5 3-8 8-8s8 3 8 8z" fill="#6f5a62"/></svg>Profil
    </div>
    <div class="header-action" style="left:1257px">
      <svg width="20" height="20" viewBox="0 0 20 20"><path d="M1 2h3l2 10h11l2-7H5" fill="none" stroke="#6f5a62" stroke-width="2"/><path d="M5.5 5h13l-2 7h-9z" fill="#6f5a62"/><circle cx="8" cy="16.5" r="1.8" fill="#6f5a62"/><circle cx="15" cy="16.5" r="1.8" fill="#6f5a62"/></svg>Warenkorb
    </div>
  </header>

  <main class="catalog">
    <h1>Produktkatalog</h1>
    <div class="filters">
      <span class="active">Alle Produkte</span><span>Katzenkratzartikel</span><span>Plüschbetten</span><span>Katzenspielzeug</span><span>Interaktive Spielzeuge</span><span>Zubehör</span>
    </div>
    <hr>
    <div class="grid">
      <article class="card"><div class="photo" role="img" aria-label="Katze auf einem türkisen Kratzsofa" style="background:linear-gradient(135deg,#3e4b49,#2f6f7a 55%,#c9a56a)"></div><h2>Kratzsofa Royal</h2><p class="price">59,99€</p><p class="stock"><i></i>Auf Lager</p><a class="btn">Zum Produkt</a></article>
      <article class="card"><div class="photo" role="img" aria-label="Rosa und blaue Filzhöhlen auf Teppich" style="background:linear-gradient(135deg,#c9d2ea,#f2c3d8 50%,#d9d6d6)"></div><h2>Filzhöhle</h2><p class="price">19,99€</p><p class="stock out"><i></i>Nicht auf Lager</p><a class="btn">Zum Produkt</a></article>
      <article class="card"><div class="photo" role="img" aria-label="Rote Spielschlange auf Holzboden" style="background:linear-gradient(160deg,#f6d1cf,#e9b386 45%,#dca06f)"></div><h2>Interaktive Spielschlange</h2><p class="price">19,99€</p><p class="stock"><i></i>Auf Lager</p><a class="btn">Zum Produkt</a></article>
      <article class="card"><div class="photo" role="img" aria-label="Bunte Plüschmäuse mit Katzenminze-Fläschchen" style="background:linear-gradient(135deg,#7fb0d8,#e8a172 45%,#9cc782 70%,#8a6047)"></div><h2>Plüschmäuse in vier Farben mit Katzenminze</h2><p class="price">4,19€</p><p class="stock"><i></i>Auf Lager</p><a class="btn">Zum Produkt</a></article>
      <article class="card"><div class="photo" role="img" aria-label="Bunte Spielbälle mit Verpackungen" style="background:linear-gradient(135deg,#f4e7ec,#f3b3c2 40%,#f3d27a 65%,#8fd0e0)"></div><h2>Spielball mit Soundchip, verschiedene Farben</h2><p class="price">4,19€</p><p class="stock"><i></i>Auf Lager</p><a class="btn">Zum Produkt</a></article>
      <article class="card"><div class="photo" role="img" aria-label="Silberner Laserpointer" style="background:linear-gradient(135deg,#fbeef2,#c8c4c6 50%,#f8edf1)"></div><h2>Laserpointer, mit verschiedenen Motiven</h2><p class="price">5,99€</p><p class="stock"><i></i>Auf Lager</p><a class="btn">Zum Produkt</a></article>
      <article class="card"><div class="photo" role="img" aria-label="Gestreifte Sisalbälle in verschiedenen Farben" style="background:linear-gradient(135deg,#f6e8ef,#b49ad8 35%,#f2a363 55%,#e070b6)"></div><h2>Sisalball</h2><p class="price">0,99€</p><p class="stock"><i></i>Auf Lager</p><a class="btn">Zum Produkt</a></article>
      <article class="card"><div class="photo" role="img" aria-label="Reizangel mit Sisalscheibe und Feder" style="background:linear-gradient(135deg,#f8eef3,#f1dde6 50%,#d8b79a)"></div><h2>Reizangel mit Glocke und Sisal-Feder-Ende</h2><p class="price">1,99€</p><p class="stock"><i></i>Auf Lager</p><a class="btn">Zum Produkt</a></article>
    </div>
  </main>

  <footer class="site-footer">
    <div class="col" style="left:176px"><h3>Links</h3><a>Home</a><a>Produktkatalog</a><a>Sale</a><a>Kontakt</a></div>
    <div class="col" style="left:397px"><h3>Produktkategorien</h3><a>Katzenkratzartikel</a><a>Plüschbetten</a><a>Katzenspielzeug</a><a>Interaktive Spielzeuge</a><a>Zubehör</a></div>
    <div class="newsletter">
      <p>Abonniere unseren Newsletter, um keine Produktneuheiten<br>oder Rabattaktionen zu verpassen!</p>
      <form><div class="field">Email Adresse eintragen</div><div class="submit">Newsletter abonnieren</div></form>
    </div>
    <hr>
    <div class="social"><span></span><span></span><span></span><span></span></div>
    <nav class="legal"><span>Impressum</span><span>Datenschutzerklärung</span><span>Cookie-Richtlinie</span><span>Zahlung &amp; Versand</span><span>Allgemeine Geschäftsbedingungen</span><span>Widerrufsrecht</span></nav>
  </footer>
</div>
</body>
</html>
```